Redesign of Grantlyhub.com

We need a redesign of some key-pages on our crowdfunding website for mobile apps, GrantlyHub.com.

- Redesign of homepage
http://www.grantlyhub.com/en

- Redesign of project submission page
http://www.grantlyhub.com/en/submit-your-app/submit-your-app

- Redesign of browsing section
http://www.grantlyhub.com/en/fund-apps

- Redesign of project funding page
http://www.grantlyhub.com/en/fund-apps/sponsor/sketch-riddler?amount=5.00

Design should be highly focused on a great user experience for users of the platform, being in principal mobile developers. So we need a great user experience for mobile developers using our service.

Benchmark designs we particularly like are:
http://www.pledgorama.com/
http://www.tradebitly.com/landing/
http://www.vomba.com/

Design should have a more 'fun, happy to get involved' factor as it has nox.
Updates

Logo's have been uploaded

Target Market(s)

mobile app developers

Industry/Entity Type

Crowdfunding

Requirements
Must have
• Submission forms must have explanation fields next to the form

Homepage should have design in whihc a introductary video can be integrated

```html
<!DOCTYPE html>
<html lang="en">
<head>
<meta charset="utf-8">
<title>GrantlyHub – Crowdfunding for Mobile Apps</title>
<link href="https://fonts.googleapis.com/css2?family=Open+Sans:wght@400;600;700;800&display=swap" rel="stylesheet">
<style>
:root{
  --brand:#1f4f8f;
  --brand-light:#2a8fd0;
  --sky:#8fd6f0;
  --sky-deep:#3aa6d8;
  --red:#d8261c;
  --green:#2fa83a;
  --nav:#3b3b3b;
  --nav-dark:#262626;
  --ink:#333;
  --muted:#777;
  --page:#e9e9e9;
  --panel:#fff;
  --footer:#2b2b2b;
  --footer-bar:#181818;
}
*{box-sizing:border-box;margin:0;padding:0}
html,body{width:720px;height:1200px;overflow:hidden}
body{font-family:"Open Sans",Arial,sans-serif;color:var(--ink);background:var(--page);position:relative;font-size:11px}
a{color:inherit;text-decoration:none}

/* header */
.site-header{position:absolute;left:0;top:0;width:720px;height:158px;background:var(--panel)}
.brand{position:absolute;left:36px;top:30px;display:flex;align-items:center;gap:12px}
.brand-mark{width:52px;height:52px;background:var(--brand-light);border-radius:6px}
.brand-name{font-size:40px;font-weight:800;color:var(--brand);letter-spacing:-1px}
.top-links{position:absolute;right:36px;top:12px;display:flex;align-items:center;gap:6px;font-size:9px;color:#555}
.top-links .sep{color:#aaa}
.search{width:56px;height:14px;border:1px solid #bbb;border-radius:3px;font-size:8px;color:#999;padding-left:4px;line-height:12px}
.social{position:absolute;right:40px;top:42px;display:flex;gap:10px}
.social span{width:22px;height:22px;border-radius:50%;background:#333;display:block}

/* main nav */
.main-nav{position:absolute;left:36px;top:158px;width:648px;height:30px;background:linear-gradient(#4a4a4a,var(--nav-dark));display:flex;align-items:center;padding-left:6px;gap:4px}
.main-nav a{color:#fff;font-size:11px;font-weight:600;padding:5px 12px;border-radius:3px}
.main-nav a.active{background:var(--brand-light)}
.main-nav .auth{margin-left:auto;display:flex;gap:6px;padding-right:6px}
.main-nav .login{background:var(--red)}
.main-nav .register{background:var(--green)}

/* hero */
.hero{position:absolute;left:0;top:190px;width:720px;height:172px;background:linear-gradient(var(--sky-deep),var(--sky))}
.hero-phones{position:absolute;left:70px;top:12px;width:250px;height:158px;background:linear-gradient(#2a2a2a,#555);border-radius:14px 14px 0 0}
.hero-video{position:absolute;left:360px;top:22px;width:290px;height:136px;background:#fff;border:5px solid #f3f3f3;box-shadow:0 2px 6px rgba(0,0,0,.25);display:flex;align-items:center;justify-content:center}
.hero-video .video-name{font-size:30px;font-weight:800;color:var(--brand)}
.hero-video .play{position:absolute;right:12px;bottom:10px}

/* tagline */
.tagline{position:absolute;left:36px;top:374px;width:648px;height:36px;display:flex;align-items:center;gap:10px}
.tagline p{font-size:11.5px;color:#444;flex:1}
.btn{display:inline-block;background:var(--red);color:#fff;font-weight:700;font-size:11px;padding:8px 12px;border-radius:4px}

/* content */
.content{position:absolute;left:36px;top:420px;width:648px;height:532px;background:var(--panel);padding:10px 12px}
.apps{position:absolute;left:12px;top:10px;width:408px}
.section-head{display:flex;justify-content:space-between;align-items:center;height:22px;margin-bottom:6px}
.section-head h2{font-size:14px;font-weight:700;color:#333}
.see-all{background:var(--red);color:#fff;font-size:8px;font-weight:700;padding:2px 5px;border-radius:2px}
.card-row{display:flex;gap:12px;margin-bottom:14px}
.app-card{width:93px;height:136px;background:#f4f4f4;border:1px solid #d4d4d4;border-radius:8px;padding:6px;display:flex;flex-direction:column}
.app-shot{height:58px;border-radius:3px}
.shot-a{background:linear-gradient(#4a8fd4,#a6d2f4)}
.shot-b{background:linear-gradient(#c43a2a,#f0d0b0)}
.shot-c{background:linear-gradient(#3a3f7a,#98a2d0)}
.shot-d{background:linear-gradient(#f0a020,#f7dc8a)}
.app-title{font-size:8px;font-weight:700;color:var(--brand-light);margin-top:4px}
.app-desc{font-size:6.5px;color:var(--muted);line-height:1.3;margin-top:2px;flex:1}
.app-bar{height:6px;background:#ddd;border-radius:3px;overflow:hidden}
.app-bar i{display:block;height:100%;background:var(--green)}

.sidebar{position:absolute;left:436px;top:10px;width:200px}
.people{display:grid;grid-template-columns:1fr 1fr;gap:6px 8px;margin-bottom:12px}
.person{display:flex;align-items:center;gap:5px;font-size:8px;color:#555}
.avatar{width:26px;height:26px;background:linear-gradient(#c9a58a,#8a6b55);border-radius:2px;flex:none}
.newsletter{background:var(--brand-light);padding:8px;color:#fff;margin-bottom:10px}
.newsletter h3{font-size:13px;margin-bottom:2px}
.newsletter p{font-size:7.5px;margin-bottom:6px}
.field{height:16px;background:#fff;color:#999;font-size:8px;padding:2px 5px;margin-bottom:5px}
.newsletter .btn{padding:3px 10px;font-size:8px}
.like-box{border:1px solid #ccc;padding:7px;font-size:7.5px;color:#555}
.like-box .row{display:flex;gap:6px;align-items:center;margin-bottom:6px}
.like-box .sq{width:28px;height:28px;background:var(--brand-light);flex:none}
.like-box .thumbs{display:flex;gap:3px;margin-top:5px}
.like-box .thumbs span{width:18px;height:18px;background:#c9b3a0}

/* footer */
.site-footer{position:absolute;left:0;top:960px;width:720px;height:216px;background:var(--footer);color:#ddd}
.announce{position:absolute;left:36px;top:12px;width:250px}
.site-footer h3{font-size:13px;color:#fff;margin-bottom:6px}
.announce h4{font-size:9.5px;color:#fff;margin-bottom:4px}
.announce p{font-size:8px;line-height:1.4;margin-bottom:6px;color:#bbb}
.partners{position:absolute;left:310px;top:12px;width:374px}
.partner-grid{display:grid;grid-template-columns:repeat(4,1fr);gap:10px}
.partner-grid span{height:62px;background:#444;border-radius:4px}
.site-footer .btn{position:absolute;bottom:12px;padding:5px 12px;font-size:9px}
.bottom-nav{position:absolute;left:0;top:1176px;width:720px;height:24px;background:var(--footer-bar);display:flex;justify-content:center;align-items:center;gap:22px;color:#fff;font-size:10px}
</style>
</head>
<body>

<header class="site-header">
  <a class="brand" href="#"><span class="brand-mark"></span><span class="brand-name">GrantlyHub</span></a>
  <nav class="top-links">
    <a href="#">Blog</a><span class="sep">|</span>
    <a href="#">Get AAA Certified</a><span class="sep">|</span>
    <a href="#">About us</a><span class="sep">|</span>
    <span class="search">Search site</span>
  </nav>
  <div class="social"><span></span><span></span><span></span></div>
</header>

<nav class="main-nav">
  <a class="active" href="#">Home</a>
  <a href="#">Fund Apps</a>
  <a href="#">Submit your App</a>
  <a href="#">Find a Developer</a>
  <a href="#">How it Works</a>
  <div class="auth"><a class="login" href="#">Login</a><a class="register" href="#">Register</a></div>
</nav>

<section class="hero">
  <div class="hero-phones" role="img" aria-label="Group of smartphones showing app screens"></div>
  <div class="hero-video">
    <span class="video-name">GrantlyHub</span>
    <svg class="play" width="26" height="26" viewBox="0 0 26 26"><circle cx="13" cy="13" r="12" fill="#2a8fd0"/><path d="M10 7l9 6-9 6z" fill="#fff"/></svg>
  </div>
</section>

<div class="tagline">
  <p>Start a project now and get fund. Support a project and contribute you too.</p>
  <a class="btn" href="#">Start a project</a>
  <a class="btn" href="#">Support projects</a>
</div>

<main class="content">
  <div class="apps">
    <section>
      <div class="section-head"><h2>Most funded Apps</h2><a class="see-all" href="#">See All</a></div>
      <div class="card-row">
        <article class="app-card"><div class="app-shot shot-a" role="img" aria-label="App screenshot"></div><div class="app-title">Sketch Riddler</div><p class="app-desc">Fun guessing game where friends sketch and solve.</p><div class="app-bar"><i style="width:80%"></i></div></article>
        <article class="app-card"><div class="app-shot shot-b" role="img" aria-label="App screenshot"></div><div class="app-title">Panda Pal</div><p class="app-desc">Fun guessing game where friends sketch and solve.</p><div class="app-bar"><i style="width:65%"></i></div></article>
        <article class="app-card"><div class="app-shot shot-c" role="img" aria-label="App screenshot"></div><div class="app-title">Moon Quest</div><p class="app-desc">Fun guessing game where friends sketch and solve.</p><div class="app-bar"><i style="width:55%"></i></div></article>
        <article class="app-card"><div class="app-shot shot-d" role="img" aria-label="App screenshot"></div><div class="app-title">Signal Hub</div><p class="app-desc">Fun guessing game where friends sketch and solve.</p><div class="app-bar"><i style="width:40%"></i></div></article>
      </div>
    </section>
    <section>
      <div class="section-head"><h2>Our Staff's pick</h2><a class="see-all" href="#">See All</a></div>
      <div class="card-row">
        <article class="app-card"><div class="app-shot shot-a" role="img" aria-label="App screenshot"></div><div class="app-title">Sketch Riddler</div><p class="app-desc">Fun guessing game where friends sketch and solve.</p><div class="app-bar"><i style="width:70%"></i></div></article>
        <article class="app-card"><div class="app-shot shot-b" role="img" aria-label="App screenshot"></div><div class="app-title">Panda Pal</div><p class="app-desc">Fun guessing game where friends sketch and solve.</p><div class="app-bar"><i style="width:50%"></i></div></article>
        <article class="app-card"><div class="app-shot shot-c" role="img" aria-label="App screenshot"></div><div class="app-title">Moon Quest</div><p class="app-desc">Fun guessing game where friends sketch and solve.</p><div class="app-bar"><i style="width:60%"></i></div></article>
        <article class="app-card"><div class="app-shot shot-d" role="img" aria-label="App screenshot"></div><div class="app-title">Signal Hub</div><p class="app-desc">Fun guessing game where friends sketch and solve.</p><div class="app-bar"><i style="width:35%"></i></div></article>
      </div>
    </section>
    <section>
      <div class="section-head"><h2>Successfully funded</h2><a class="see-all" href="#">See All</a></div>
      <div class="card-row">
        <article class="app-card"><div class="app-shot shot-a" role="img" aria-label="App screenshot"></div><div class="app-title">Sketch Riddler</div><p class="app-desc">Fun guessing game where friends sketch and solve.</p><div class="app-bar"><i style="width:100%"></i></div></article>
        <article class="app-card"><div class="app-shot shot-b" role="img" aria-label="App screenshot"></div><div class="app-title">Panda Pal</div><p class="app-desc">Fun guessing game where friends sketch and solve.</p><div class="app-bar"><i style="width:100%"></i></div></article>
        <article class="app-card"><div class="app-shot shot-c" role="img" aria-label="App screenshot"></div><div class="app-title">Moon Quest</div><p class="app-desc">Fun guessing game where friends sketch and solve.</p><div class="app-bar"><i style="width:100%"></i></div></article>
        <article class="app-card"><div class="app-shot shot-d" role="img" aria-label="App screenshot"></div><div class="app-title">Signal Hub</div><p class="app-desc">Fun guessing game where friends sketch and solve.</p><div class="app-bar"><i style="width:100%"></i></div></article>
      </div>
    </section>
  </div>

  <aside class="sidebar">
    <div class="section-head"><h2>Most active funders</h2></div>
    <div class="people">
      <div class="person"><span class="avatar" role="img" aria-label="Member photo"></span>Elliot R.</div>
      <div class="person"><span class="avatar" role="img" aria-label="Member photo"></span>Elliot R.</div>
      <div class="person"><span class="avatar" role="img" aria-label="Member photo"></span>Elliot R.</div>
      <div class="person"><span class="avatar" role="img" aria-label="Member photo"></span>Elliot R.</div>
      <div class="person"><span class="avatar" role="img" aria-label="Member photo"></span>Elliot R.</div>
      <div class="person"><span class="avatar" role="img" aria-label="Member photo"></span>Elliot R.</div>
      <div class="person"><span class="avatar" role="img" aria-label="Member photo"></span>Elliot R.</div>
      <div class="person"><span class="avatar" role="img" aria-label="Member photo"></span>Elliot R.</div>
    </div>
    <div class="section-head"><h2>New Members</h2></div>
    <div class="people">
      <div class="person"><span class="avatar" role="img" aria-label="Member photo"></span>Elliot R.</div>
      <div class="person"><span class="avatar" role="img" aria-label="Member photo"></span>Elliot R.</div>
      <div class="person"><span class="avatar" role="img" aria-label="Member photo"></span>Elliot R.</div>
      <div class="person"><span class="avatar" role="img" aria-label="Member photo"></span>Elliot R.</div>
      <div class="person"><span class="avatar" role="img" aria-label="Member photo"></span>Elliot R.</div>
      <div class="person"><span class="avatar" role="img" aria-label="Member photo"></span>Elliot R.</div>
    </div>
    <div class="newsletter">
      <h3>Newsletter</h3>
      <p>Sign up here to receive regular e-newsletter</p>
      <div class="field">Email</div>
      <div class="field">Name</div>
      <a class="btn" href="#">Submit</a>
    </div>
    <div class="like-box">
      <div class="row"><span class="sq"></span><span>GrantlyHub - Crowdfunding Mobile Apps</span></div>
      <p>1,052 people like GrantlyHub - Crowdfunding Mobile Apps.</p>
      <div class="thumbs"><span></span><span></span><span></span><span></span><span></span><span></span></div>
    </div>
  </aside>
</main>

<footer class="site-footer">
  <div class="announce">
    <h3>Book Announcements</h3>
    <h4>Got some spare 2 hours/week?</h4>
    <p>Volunteer with our team on these programs and help young developers build their first mobile apps this year.</p>
    <p>Study with us for Apps Services or Mobile Care, join our Community Services course for free this term.</p>
    <p>Join our product Friday team, where every Friday we review new submissions live with founders.</p>
  </div>
  <a class="btn" href="#" style="left:36px">Learn More</a>
  <div class="partners">
    <h3>Partners</h3>
    <div class="partner-grid"><span></span><span></span><span></span><span></span><span></span><span></span><span></span><span></span></div>
  </div>
  <a class="btn" href="#" style="right:36px">Learn More</a>
</footer>

<nav class="bottom-nav">
  <a href="#">Home</a><a href="#">Fund Apps</a><a href="#">Submit your App</a><a href="#">Find a Developer</a><a href="#">How it Works</a>
</nav>

</body>
</html>
```